Astrologer needs a design for business card

I need a business card design for my job in astrology and flower therapy.
In front side need the information add file.

In back side need the informations above:
INTERPRETAÇÕES
TENDÊNCIAS
AUTOCONHECIMENTO
ANÁLISE VOCACIONAL
DIRECIONAMENTO DE CARREIRA
RELACIONAMENTOS
ASTROLOGIA EMPRESARIAL
TERAPIA FLORAL – Florias de Dorsk e Rui Tavenco

Business

OVRA

```html
<!DOCTYPE html>
<html lang="pt">
<head>
<meta charset="utf-8">
<title>Elvarin Stolz – Cartão de visita</title>
<link rel="stylesheet" href="https://fonts.googleapis.com/css2?family=Archivo+Narrow:wght@700&family=Marcellus&family=Roboto:wght@300&display=swap">
<style>
  :root {
    --page: #e9e8ec;
    --card: #7e768a;
    --band: #c7c0d8;
    --ink-light: #c4bdd4;
    --ink-dark: #7e768a;
    --rule: #a59db3;
  }
  * { margin: 0; padding: 0; box-sizing: border-box; }
  html, body { width: 1200px; height: 900px; overflow: hidden; background: var(--page); }
  .canvas { position: relative; width: 1200px; height: 900px; }

  .card {
    position: absolute; top: 276px; width: 540px; height: 348px;
    background: var(--card);
    box-shadow: 0 6px 18px rgba(40, 30, 55, .25);
  }
  .card--front { left: 40px; }
  .card--back { left: 620px; }

  .name { font-family: "Archivo Narrow", "Arial Narrow", sans-serif; font-weight: 700; line-height: .9; }
  .name__first { display: block; }
  .name__last { display: block; font-size: .62em; }

  /* Front */
  .band {
    position: absolute; left: 0; right: 0; top: 113px; height: 111px;
    background: var(--band); color: var(--ink-dark);
  }
  .band .name { position: absolute; left: 28px; top: 22px; width: 152px; text-align: right; font-size: 42px; }
  .band__rule { position: absolute; left: 190px; top: 22px; width: 1px; height: 66px; background: var(--ink-dark); }
  .services { position: absolute; left: 203px; top: 24px; font-family: "Marcellus", serif; line-height: 1; }
  .services__line { display: block; font-size: 23px; letter-spacing: .3px; }
  .services__line--large { font-size: 31px; margin-top: 4px; }

  /* Back */
  .card--back .name { position: absolute; left: 44px; top: 90px; font-size: 44px; color: var(--ink-light); }
  .contact { position: absolute; left: 272px; top: 112px; font-family: "Roboto", sans-serif; font-weight: 300; color: var(--ink-light); }
  .contact__row { display: flex; align-items: center; gap: 9px; }
  .contact__row--phone { font-size: 21px; }
  .contact__row--mail { font-size: 15px; margin-top: 6px; }
  .contact svg { flex: none; }

  .topics { position: absolute; left: 0; top: 0; width: 540px; height: 348px; font-family: "Marcellus", serif; color: var(--ink-light); }
  .topic { position: absolute; top: 264px; line-height: 24px; white-space: nowrap; }
  .topic__title { display: block; font-size: 18px; }
  .topic__item { display: block; font-size: 13px; }
  .topic__item--compact { font-size: 11.5px; letter-spacing: -.2px; }
  .topic__item--large { font-size: 15px; }
  .topic--interpretations { left: 12px; width: 164px; text-align: right; }
  .topic--trends { left: 184px; width: 122px; text-align: center; }
  .topic--self { left: 314px; width: 216px; text-align: center; }
  .topic__footnote { position: absolute; right: 236px; top: 312px; line-height: 24px; font-size: 12px; white-space: nowrap; }
  .topics__rule { position: absolute; width: 1px; background: var(--rule); }
  .topics__rule--first { left: 180px; top: 266px; height: 46px; }
  .topics__rule--second { left: 310px; top: 266px; height: 70px; }
</style>
</head>
<body>
<main class="canvas">
  <section class="card card--front" aria-label="Frente do cartão">
    <div class="band">
      <div class="name"><span class="name__first">Elvarin</span><span class="name__last">Stolz</span></div>
      <div class="band__rule"></div>
      <p class="services">
        <span class="services__line">MAPAS ASTROLÓGICOS</span>
        <span class="services__line services__line--large">TERAPIA FLORAL</span>
      </p>
    </div>
  </section>

  <section class="card card--back" aria-label="Verso do cartão">
    <div class="name"><span class="name__first">Elvarin</span><span class="name__last">Stolz</span></div>
    <div class="contact">
      <p class="contact__row contact__row--phone">
        <svg width="12" height="20" viewBox="0 0 12 20" aria-hidden="true"><rect x="1" y="1" width="10" height="18" rx="2" fill="none" stroke="currentColor" stroke-width="1.5"/><line x1="4" y1="16" x2="8" y2="16" stroke="currentColor" stroke-width="1.2"/></svg>
        (51) 9000-5172
      </p>
      <p class="contact__row contact__row--mail">
        <svg width="14" height="10" viewBox="0 0 14 10" aria-hidden="true"><rect x="0" y="0" width="14" height="10" fill="currentColor"/><polyline points="0,0 7,6 14,0" fill="none" stroke="var(--card)" stroke-width="1.2"/></svg>
        elvarinstolz@mailbox.com
      </p>
    </div>
    <div class="topics">
      <div class="topic topic--interpretations">
        <span class="topic__title">INTERPRETAÇÕES</span>
        <span class="topic__item">ANÁLISE VOCACIONAL</span>
      </div>
      <span class="topics__rule topics__rule--first"></span>
      <div class="topic topic--trends">
        <span class="topic__title">TENDÊNCIAS</span>
        <span class="topic__item">RELACIONAMENTOS</span>
      </div>
      <span class="topics__rule topics__rule--second"></span>
      <div class="topic topic--self">
        <span class="topic__title">AUTOCONHECIMENTO</span>
        <span class="topic__item topic__item--compact">DIRECIONAMENTO DE CARREIRA</span>
        <span class="topic__item topic__item--large">ASTROLOGIA EMPRESARIAL</span>
      </div>
      <p class="topic__footnote">TERAPIA FLORAL – Florias de Dorsk e Rui Tavenco</p>
    </div>
  </section>
</main>
</body>
</html>
```